create a more innovative version of our powerpoint presentation

We built A 14-pages powerpoint document. We would like to change the look of this document. We work in digital area. So, we would like something more modern, more current and less classical. We need to be fashionable while remaining reassuring for corporate. Our business is to make recommendations in 5 days where our competitors do it in 3 months and after to support companies with this "fern'kite" proposition.

Target Market(s)

medium sized business, or a large global enterprise

Industry/Entity Type

Digital

Colors

Requirements
Must have
• We are working with digital expert. We need to surprise them.

```html
<!DOCTYPE html>
<html lang="fr">
<head>
<meta charset="utf-8">
<title>fern'kite — Accompagner la Transformation</title>
<link href="https://fonts.googleapis.com/css2?family=PT+Sans:wght@400;700&display=swap" rel="stylesheet">
<style>
  :root {
    --teal: #2bb1ae;
    --teal-light: #4cc7c4;
    --teal-dark: #1d8f8c;
    --navy: #1b2858;
    --orange: #f4a761;
    --orange-dark: #d9843c;
    --grey-text: #6d7478;
    --grey-line: #e6e9ea;
    --page: #ffffff;
  }
  * { box-sizing: border-box; margin: 0; padding: 0; }
  html, body { width: 1200px; height: 2894px; overflow: hidden; background: var(--page); }
  body { font-family: "PT Sans", Arial, sans-serif; position: relative; }

  .slide {
    position: absolute; left: 192px; width: 817px; height: 460px;
    background: #fff; overflow: hidden;
    box-shadow: 0 3px 10px rgba(0,0,0,0.28);
  }
  .abs { position: absolute; }

  .brand { position: absolute; display: flex; align-items: center; gap: 6px;
    font-weight: 700; color: var(--navy); white-space: nowrap; }
  .brand-square { width: 12px; height: 12px; background: var(--orange); }
  .brand-top { left: 50%; top: 38px; transform: translateX(-50%); font-size: 22px; }
  .brand-foot { left: 30px; top: 408px; font-size: 15px; }
  .brand-foot .brand-square { width: 9px; height: 9px; }

  .cover-band { position: absolute; left: 0; right: 0; background: var(--teal); }
  .cover-title { position: absolute; color: #fff; font-weight: 700; }
  .slide-1 .cover-band { top: 112px; bottom: 0; }
  .slide-1 .illustration { left: 70px; top: 175px; width: 170px; height: 235px;
    background: linear-gradient(160deg, rgba(255,255,255,0.18), rgba(0,0,0,0.06)); border-radius: 4px; }
  .slide-1 .cover-title { left: 313px; top: 170px; font-size: 47px; line-height: 55px; }

  .slide-2 .cover-band { top: 108px; bottom: 0;
    background: linear-gradient(100deg, #7cc6c2 0%, #3fb4b0 40%, #2fa9a6 70%, #4bbab6 100%); }
  .slide-2 .cover-title { left: 0; right: 0; top: 180px; text-align: center; font-size: 41px; line-height: 50px; }

  .top-accent { position: absolute; top: 0; left: 50%; transform: translateX(-50%);
    width: 122px; height: 13px; background: var(--orange); }
  .slide-title { position: absolute; left: 0; right: 0; top: 22px; text-align: center;
    color: var(--navy); font-weight: 700; font-size: 31px; }

  .footer-line { position: absolute; left: 120px; right: 70px; top: 424px; height: 1px; background: var(--grey-line); }
  .footer-meta { position: absolute; top: 432px; font-size: 10px; color: #aab0b3; letter-spacing: 0.5px; }
  .page-num { position: absolute; right: 40px; top: 418px; font-size: 16px; font-weight: 700; color: var(--teal); }

  .row { position: absolute; left: 0; width: 690px; height: 64px; }
  .row svg { position: absolute; left: 0; top: 0; }
  .row-tab { position: absolute; left: 0; top: -4px; width: 174px; height: 60px;
    display: flex; align-items: center; justify-content: center; text-align: center;
    color: #fff; font-weight: 700; font-size: 16px; line-height: 18px; }
  .row-list { position: absolute; left: 225px; top: 0; height: 64px; display: flex; flex-direction: column;
    justify-content: center; color: #fff; font-size: 16px; line-height: 21px; list-style: none; }
  .row-list li::before { content: "•"; margin-right: 8px; }

  .cloud { position: absolute; left: 262px; top: 92px; width: 294px; height: 294px; border-radius: 50%;
    background: radial-gradient(circle at 45% 40%, #eef5f6 0%, #cfe6ea 55%, #b9dbe0 100%); }

  .photo { position: absolute; }
  .slide-5 .side-photo { left: 0; top: 0; width: 219px; height: 460px;
    background: linear-gradient(160deg, #6fcfcc 0%, #33b3b0 45%, #239e9b 100%); }
  .side-heading { position: absolute; left: 33px; top: 163px; color: #fff; font-weight: 700; font-size: 29px; line-height: 35px; }
  .side-underline { position: absolute; left: 139px; top: 282px; width: 56px; height: 4px; background: var(--orange); }
  .q-list { position: absolute; left: 238px; top: 12px; list-style: none; }
  .q-item { position: absolute; left: 0; display: flex; align-items: center; gap: 12px; width: 560px;
    font-size: 13.5px; line-height: 16px; color: var(--grey-text); }
  .q-icon { flex: none; width: 28px; height: 28px; border-radius: 50%; background: var(--teal);
    display: flex; align-items: center; justify-content: center; }
  .slide-5 .city-photo { left: 219px; top: 271px; width: 598px; height: 150px;
    background: linear-gradient(180deg, #d9d9d9 0%, #9a9a9a 45%, #3c3c3c 100%); }

  .slide-6 .side-photo { left: 0; top: 0; width: 168px; height: 460px;
    background: linear-gradient(170deg, #8fb3d6 0%, #5b6f86 45%, #3b4048 100%); }
  .slide-6 .side-panel { position: absolute; left: 168px; top: 0; width: 220px; height: 460px; background: var(--teal); }
  .panel-item { position: absolute; left: 190px; width: 180px; color: #fff; font-size: 13px; line-height: 16px; }
  .panel-item svg { display: block; margin-bottom: 8px; }
  .imp-title { position: absolute; left: 406px; top: 30px; color: var(--navy); font-weight: 700; font-size: 29px; }
  .imp-underline { position: absolute; left: 406px; top: 72px; width: 56px; height: 4px; background: var(--orange); }
  .imp-item { position: absolute; left: 408px; color: var(--grey-text); font-size: 13px; }
  .imp-item svg { display: block; margin: 0 0 6px 16px; }
</style>
</head>
<body>

<section class="slide slide-1" style="top:10px">
  <div class="brand brand-top"><span class="brand-square"></span>fern'kite</div>
  <div class="cover-band"></div>
  <div class="abs illustration" role="img" aria-label="Line drawing of a figure striding forward"></div>
  <h1 class="cover-title">Accompagner la<br>Transformation<br>des personnes et<br>des organisations</h1>
</section>

<section class="slide slide-2" style="top:492px">
  <div class="brand brand-top"><span class="brand-square"></span>fern'kite</div>
  <div class="cover-band" role="img" aria-label="Teal-tinted photo of a hand reaching toward a digital network"></div>
  <h1 class="cover-title">Accompagner la<br>Transformation<br>des personnes et des<br>organisations</h1>
</section>

<section class="slide slide-3" style="top:974px">
  <div class="top-accent"></div>
  <h2 class="slide-title">fern'kite</h2>

  <div class="row" style="top:112px">
    <svg width="690" height="72"><polygon points="160,0 660,0 690,32 660,64 160,64" fill="var(--teal-light)"/><polygon points="160,56 174,56 174,68" fill="var(--teal-dark)"/></svg>
    <div class="row-tab" style="background:var(--teal)">Evoluer<br>autrement</div>
    <ul class="row-list"><li>Anticiper</li><li>Ré-inventer</li></ul>
  </div>
  <div class="row" style="top:198px">
    <svg width="690" height="72"><polygon points="160,0 660,0 690,32 660,64 160,64" fill="var(--orange)"/><polygon points="160,56 174,56 174,68" fill="var(--orange-dark)"/></svg>
    <div class="row-tab" style="background:var(--orange)">Avec la Marque</div>
    <ul class="row-list"><li>comme point d'appui</li></ul>
  </div>
  <div class="row" style="top:282px">
    <svg width="690" height="72"><polygon points="160,0 660,0 690,32 660,64 160,64" fill="var(--teal-light)"/><polygon points="160,56 174,56 174,68" fill="var(--teal-dark)"/></svg>
    <div class="row-tab" style="background:var(--teal)">Pour<br>accompagner</div>
    <ul class="row-list"><li>Les Personnes</li><li>Et les Organisations</li></ul>
  </div>

  <div class="brand brand-foot"><span class="brand-square"></span>fern'kite</div>
  <div class="footer-line"></div>
  <div class="footer-meta" style="left:340px">11/02/2018 &nbsp;&nbsp;|&nbsp;&nbsp; FK</div>
  <div class="page-num">3</div>
</section>

<section class="slide slide-4" style="top:1456px">
  <div class="top-accent"></div>
  <h2 class="slide-title">Le monde se transforme inexorablement!</h2>

  <div class="cloud" role="img" aria-label="Circular word cloud of digital trend keywords in teal, navy and orange"></div>

  <div class="brand brand-foot"><span class="brand-square"></span>fern'kite</div>
  <div class="footer-line"></div>
  <div class="footer-meta" style="left:340px">11/02/2018 &nbsp;&nbsp;|&nbsp;&nbsp; FK</div>
  <div class="page-num">4</div>
</section>

<section class="slide slide-5" style="top:1938px">
  <div class="photo side-photo" role="img" aria-label="Teal-tinted photo of a glass office tower"></div>
  <h2 class="side-heading">Répondre à<br>de nouvelles<br>questions !</h2>
  <div class="side-underline"></div>

  <ul class="q-list">
    <li class="q-item" style="top:0"><span class="q-icon"><svg width="16" height="16"><circle cx="5" cy="5" r="3" fill="none" stroke="#fff" stroke-width="1.5"/><circle cx="11" cy="11" r="3" fill="none" stroke="#fff" stroke-width="1.5"/></svg></span>Comment les organisations s'adaptent-elles face aux indispensables<br>transformations ? .</li>
    <li class="q-item" style="top:48px"><span class="q-icon"><svg width="16" height="16"><rect x="3" y="2" width="10" height="12" rx="1" fill="none" stroke="#fff" stroke-width="1.5"/><line x1="5" y1="6" x2="11" y2="6" stroke="#fff"/><line x1="5" y1="9" x2="11" y2="9" stroke="#fff"/></svg></span>Par quel bout commencer ?</li>
    <li class="q-item" style="top:86px"><span class="q-icon"><svg width="16" height="16"><rect x="4" y="2" width="8" height="12" rx="1.5" fill="none" stroke="#fff" stroke-width="1.5"/><circle cx="8" cy="11" r="1" fill="#fff"/></svg></span>Comment embarquer les équipes dans tous ces changements ?</li>
    <li class="q-item" style="top:124px"><span class="q-icon"><svg width="16" height="16"><path d="M2 4h2l2 7h7l2-5H5" fill="none" stroke="#fff" stroke-width="1.5"/><circle cx="7" cy="14" r="1" fill="#fff"/><circle cx="12" cy="14" r="1" fill="#fff"/></svg></span>Comment &nbsp;maintenir la motivation des collaborateurs?</li>
    <li class="q-item" style="top:172px"><span class="q-icon"><svg width="16" height="16"><rect x="2" y="3" width="12" height="10" rx="1" fill="none" stroke="#fff" stroke-width="1.5"/><path d="M5 8l2 2 4-4" fill="none" stroke="#fff" stroke-width="1.5"/></svg></span>Comment l'individu se retrouve-t-il face à cette transformation ?</li>
    <li class="q-item" style="top:218px"><span class="q-icon"><svg width="16" height="16"><circle cx="8" cy="8" r="5.5" fill="none" stroke="#fff" stroke-width="1.5"/><path d="M5.5 8l2 2 3-4" fill="none" stroke="#fff" stroke-width="1.5"/></svg></span>Comment savoir si on a pris les bonnes décisions?</li>
  </ul>

  <div class="photo city-photo" role="img" aria-label="Black and white photo of a city skyline"></div>
  <div class="footer-meta" style="left:640px">11-Feb-19 &nbsp;&nbsp;|&nbsp;&nbsp; FK</div>
  <div class="page-num" style="right:36px;top:426px;font-size:14px">5</div>
</section>

<section class="slide slide-6" style="top:2420px">
  <div class="photo side-photo" role="img" aria-label="Upward view of a glass skyscraper against the sky"></div>
  <div class="side-panel"></div>

  <div class="panel-item" style="top:128px">
    <svg width="30" height="30"><circle cx="15" cy="15" r="12" fill="none" stroke="#fff" stroke-width="1.5"/><path d="M15 8v7l5 3" fill="none" stroke="#fff" stroke-width="1.5"/></svg>
    Complexité permanente
  </div>
  <div class="panel-item" style="top:228px">
    <svg width="30" height="30"><rect x="7" y="4" width="16" height="6" fill="none" stroke="#fff" stroke-width="1.5"/><rect x="7" y="12" width="16" height="6" fill="none" stroke="#fff" stroke-width="1.5"/><line x1="15" y1="18" x2="15" y2="28" stroke="#fff" stroke-width="1.5"/></svg>
    Nouveaux repères
  </div>
  <div class="panel-item" style="top:314px">
    <svg width="30" height="30"><circle cx="15" cy="15" r="5" fill="none" stroke="#fff" stroke-width="1.5"/><circle cx="15" cy="15" r="11" fill="none" stroke="#fff" stroke-width="1.5" stroke-dasharray="4 3"/></svg>
    Repenser les marques qui<br>appartiennent aussi aux<br>clients
  </div>

  <h2 class="imp-title">De nouveaux impératifs</h2>
  <div class="imp-underline"></div>

  <div class="imp-item" style="top:168px">
    <svg width="30" height="30"><path d="M15 4c-5 0-8 4-8 8 0 6 3 7 3 11h10c0-4 3-5 3-11 0-4-3-8-8-8z" fill="none" stroke="var(--teal)" stroke-width="1.5"/><line x1="11" y1="27" x2="19" y2="27" stroke="var(--teal)" stroke-width="1.5"/></svg>
    Besoin de sens
  </div>
  <div class="imp-item" style="top:246px">
    <svg width="34" height="30"><circle cx="8" cy="10" r="4" fill="none" stroke="var(--teal)" stroke-width="1.5"/><circle cx="26" cy="10" r="4" fill="none" stroke="var(--teal)" stroke-width="1.5"/><circle cx="17" cy="22" r="4" fill="none" stroke="var(--teal)" stroke-width="1.5"/><path d="M11 13l4 6M23 13l-4 6M12 10h10" stroke="var(--teal)" stroke-width="1.5"/></svg>
    Nouvelles synergies
  </div>

  <div class="footer-meta" style="left:640px">11-Feb-19 &nbsp;&nbsp;|&nbsp;&nbsp; FK</div>
  <div class="page-num" style="right:36px;top:426px;font-size:14px">6</div>
</section>

</body>
</html>
```